Professional Services/Construction Management (Millwork) Biz Cards

We've decided on a logo and have our color palette set, now we want to design some very professional looking cards that make a strong first impression - they'll reflect our tagline (that we're going to put on the back: Innovative. Professional. Leaders.

The example business card shows generally the direction we've been thinking of going for the back side - **but we're open to other ideas**

Target Market(s)

The cards should target more high-end (wealthy) owners and general contracting companies. We want them to convey a strong first impression - in a professional and not garish way.

Industry/Entity Type

Construction Company

Contact Information for Business Card

There needs to be a place for our company contractor's license number and business address. We want to also have people's names, titles, phone number, email address. The back can be the logo, tagline and web address

Requirements
Must have
• follow our color palette
Nice to have
• Font & Styles should compliment the Harbor Joinery fonts, but not necessarily match exactly

```html
<!DOCTYPE html>
<html lang="en">
<head>
<meta charset="utf-8">
<title>Harbor Joinery Business Cards</title>
<link rel="stylesheet" href="https://fonts.googleapis.com/css2?family=Source+Sans+3:wght@400;600;700&display=swap">
<style>
  :root {
    --navy: #1b2f5c;
    --slate: #86878b;
    --text-grey: #6f7073;
    --paper: #ffffff;
    --backdrop: #1c1c1c;
  }
  * { margin: 0; padding: 0; box-sizing: border-box; }
  html, body { width: 1200px; height: 900px; overflow: hidden; }
  body {
    background: var(--backdrop);
    font-family: "Source Sans 3", sans-serif;
    position: relative;
  }
  .card {
    position: absolute;
    top: 170px;
    width: 347px;
    height: 561px;
    overflow: hidden;
  }
  .card-front { left: 259px; background: var(--paper); text-align: center; }
  .card-back { left: 631px; background: var(--navy); text-align: center; color: var(--paper); }

  .accent-tab {
    position: absolute;
    left: 102px;
    width: 143px;
    height: 30px;
    background: var(--navy);
  }
  .accent-tab.top { top: 0; }
  .accent-tab.bottom { bottom: 0; height: 28px; }

  .brand-mark {
    position: absolute;
    top: 88px;
    left: 0;
    width: 100%;
  }
  .brand-mark .mark-circle {
    width: 110px;
    height: 110px;
    margin: 0 auto;
    border-radius: 50%;
    background: var(--navy);
  }
  .brand-mark .brand-name {
    margin-top: 14px;
    font-size: 19px;
    font-weight: 700;
    letter-spacing: 1.5px;
    color: var(--navy);
  }

  .contact { position: absolute; top: 286px; left: 0; width: 100%; color: var(--text-grey); font-size: 15.5px; line-height: 20px; }
  .person-name { font-size: 19px; font-weight: 600; color: var(--navy); line-height: 24px; }
  .person-title { margin-bottom: 13px; }
  .address { margin-bottom: 12px; }
  .licence { margin-bottom: 12px; }
  .licence .label { color: var(--navy); }
  .contact-line { display: flex; justify-content: center; align-items: center; gap: 7px; }
  .contact-line svg { fill: var(--navy); }

  .back-name {
    position: absolute;
    top: 108px;
    width: 100%;
    font-size: 36px;
    font-weight: 700;
    letter-spacing: 3px;
    line-height: 42px;
  }
  .tagline { position: absolute; top: 216px; width: 100%; font-size: 16px; }
  .website { position: absolute; top: 245px; width: 100%; font-size: 16px; }
  .mountain-art {
    position: absolute;
    left: 0;
    bottom: 0;
    width: 100%;
    height: 241px;
    background: linear-gradient(to bottom, var(--navy) 0%, var(--slate) 45%, var(--slate) 100%);
  }
</style>
</head>
<body>
  <section class="card card-front">
    <div class="accent-tab top"></div>
    <div class="brand-mark">
      <div class="mark-circle"></div>
      <div class="brand-name">HARBOR JOINERY</div>
    </div>
    <div class="contact">
      <div class="person-name">Daniel Whitcombe</div>
      <div class="person-title">Managing Director</div>
      <div class="address">48 Quayside Lane<br>Portmoor, 204817.</div>
      <div class="licence"><span class="label">Lic Number:</span> 12345678</div>
      <div class="contact-line">
        <svg width="13" height="13" viewBox="0 0 24 24" aria-hidden="true"><path d="M6.6 10.8a15.1 15.1 0 0 0 6.6 6.6l2.2-2.2a1 1 0 0 1 1-.25 11.4 11.4 0 0 0 3.6.57 1 1 0 0 1 1 1V20a1 1 0 0 1-1 1A17 17 0 0 1 3 4a1 1 0 0 1 1-1h3.5a1 1 0 0 1 1 1c0 1.25.2 2.45.57 3.57a1 1 0 0 1-.25 1z"/></svg>
        <span>044-310 772 458</span>
      </div>
      <div class="contact-line">
        <svg width="12" height="9" viewBox="0 0 12 9" aria-hidden="true"><path d="M0 0h12v9H0z"/><path d="M0.5 0.5 6 5l5.5-4.5" fill="none" stroke="#fff" stroke-width="1"/></svg>
        <span>hello@harborjoinery.com</span>
      </div>
    </div>
    <div class="accent-tab bottom"></div>
  </section>

  <section class="card card-back">
    <div class="back-name">HARBOR JOINERY</div>
    <div class="tagline">Innovative. Professional. Leaders</div>
    <div class="website">www.harborjoinery.com</div>
    <div class="mountain-art" role="img" aria-label="Grey mountain range silhouette rising along the bottom of the card"></div>
  </section>
</body>
</html>
```